Plakate für Haushaltshilfen und Alltagsbegleiter
Zielgruppe
Wir bieten haushaltsnahe Dienstleistungen (Haushaltshilfen und Altgasbegleiter) für Personen mit einem Pflegegrad 1 - 5 an.
Zielgruppe sind Personen mit einem Pflegegrad 1 - 5. Hauptsächlich ältere Menschen die Unterstützung/Betreuung im Alltag und Haushalt benötigen.
Aufgabenstellung
Wir benötigen für unsere Büroräume eine Fensterbeschriftung. Es handelt sich hier um 5 Fenster (Glasflächen) und eine Glastür. Die Vorgabe ist, dass von außen zu erkennen ist dass sich um alle Räumlichkeiten um unsere (Firma Lindwerk) Räumlichkeiten handelt. Desweiteren soll auch unser Angebot erkennbar sein.
Unser Angebot enthält: Haushaltshilfen und Alltagsbegleiter
- kostenlose Haushaltshilfe ab Pflegegrad 1
- Abrechnung mit allen Kostenträgern
Da wir keine Schilder an die Fassade anbringen können, müßen die Glasflächen dafür genutzt werden um zum Einen uns als Firma erkennbar zu machen und zum anderen unser Angebot kurz zu präsentieren.
Uns ist wichtig dass unser Logo verwendet wir und auch unsere Farben.
Desweiteren sollten an den Fenstern auch teilweise eine Sichtschutz nach innen, angebracht werden, aber eben nur teilweise also nicht das ganzen Fenster z.Bsp. mit einer Blickdichten Folie überziehen, sondern in Augenhöhe wenn Fußgänger vorbei laufen.

```html
<!DOCTYPE html>
<html lang="de">
<head>
<meta charset="utf-8">
<title>Lindwerk – Fensterbeschriftung</title>
<link rel="stylesheet" href="https://fonts.googleapis.com/css2?family=Cinzel:wght@600;700&family=Montserrat:wght@500;700;800&display=swap">
<style>
  :root{
    --red:#c8202f;
    --red-dark:#9e1622;
    --ink:#2e2e30;
    --ink-soft:#3c3c3e;
    --white:#ffffff;
    --paper:#f4f5f6;
    --stage:#c6c6c6;
    --frame:#9b9b9b;
    --frame-light:#b3b3b3;
  }
  *{box-sizing:border-box;margin:0;padding:0}
  html,body{width:1200px;height:2235px;overflow:hidden}
  body{background:var(--stage);position:relative;font-family:"Montserrat",sans-serif}

  .window-frame{position:absolute;background:linear-gradient(180deg,var(--frame-light),var(--frame));}
  .window-frame--top{left:52px;top:330px;width:1096px;height:504px}
  .window-frame--bottom{left:52px;top:930px;width:1096px;height:586px}
  .window-frame--door{left:412px;top:930px;width:376px;height:820px}

  .poster{position:absolute;overflow:hidden;background:linear-gradient(180deg,var(--white),var(--paper) 60%,#e9ebee);text-align:center;color:var(--ink)}
  .poster__shapes{position:absolute;inset:0;width:100%;height:100%}
  .poster > *:not(.poster__shapes){position:absolute;left:0;right:0}

  .poster--offer{top:348px;width:344px;height:468px}
  .poster--offer:nth-of-type(4){left:70px}
  .offer-1{left:70px}.offer-2{left:428px}.offer-3{left:786px}

  .brand-name{font-family:"Cinzel",serif;font-weight:700;color:var(--ink-soft);letter-spacing:1px}
  .brand-tagline{font-family:"Cinzel",serif;font-weight:600;color:var(--red);letter-spacing:.5px}
  .poster--offer .brand-name{top:18px;font-size:40px}
  .poster--offer .brand-tagline{top:66px;font-size:14px}

  .emblem{margin:0 auto;border:7px solid var(--red);border-radius:50%}
  .poster--offer .emblem{top:96px;width:116px;height:116px}

  .offer-text{font-family:"Cinzel",serif;font-weight:700;font-size:19px;line-height:1.15;color:var(--ink-soft);padding:0 16px}
  .offer-text .accent{color:var(--red)}
  .poster--offer .offer-text{top:244px}

  .cta-label{font-size:10px;font-weight:500;color:var(--white)}
  .cta-phone{display:flex;align-items:center;justify-content:center;gap:6px;font-weight:800;font-size:25px;color:var(--white)}
  .cta-web{font-size:10px;font-weight:700;letter-spacing:3px;color:var(--white)}
  .poster--offer .cta-label{top:398px}
  .poster--offer .cta-phone{top:411px}
  .poster--offer .cta-web{top:446px}
  .phone-icon{width:22px;height:22px;flex:none}

  .poster--info{top:948px;width:344px;height:550px;background:var(--ink)}
  .info-1{left:70px}.info-2{left:786px}
  .info-head{top:0;height:82px;display:flex;align-items:center;justify-content:center;gap:12px}
  .info-head .dot{width:38px;height:38px;border:4px solid var(--white);border-radius:50%}
  .info-head .brand-name{position:static;color:var(--white);font-size:28px;line-height:1}
  .info-head .brand-tagline{position:static;color:var(--white);font-size:9px;display:block;margin-top:2px}
  .info-head .lockup{text-align:left}
  .info-text{font-family:"Cinzel",serif;font-weight:700;font-size:18px;line-height:1.12;color:var(--red);padding:0 26px}
  .info-text .dark{color:var(--ink-soft)}
  .info-1 .info-text{top:118px}
  .info-2 .info-text{top:118px}
  .info-2 .info-sub{top:214px;font-family:"Cinzel",serif;font-weight:700;font-size:18px;line-height:1.15;color:var(--ink-soft);padding:0 40px}
  .poster--info .emblem{top:316px;width:118px;height:118px}

  .poster--door{left:428px;top:948px;width:344px;height:784px;background:var(--ink)}
  .poster--door .emblem{top:220px;width:130px;height:130px}
  .poster--door .brand-name{top:372px;font-size:46px}
  .poster--door .brand-tagline{top:426px;font-size:16px}
  .poster--door .cta-label{top:464px;color:var(--red);font-weight:700}
  .door-phone{top:482px;margin:0 auto;width:262px;height:44px;border:3px solid var(--red);border-radius:24px;display:flex;align-items:center;justify-content:center;gap:6px;font-weight:800;font-size:24px;color:var(--ink)}
</style>
</head>
<body>

<div class="window-frame window-frame--top"></div>
<div class="window-frame window-frame--bottom"></div>
<div class="window-frame window-frame--door"></div>

<!-- Row 1: offer posters -->
<section class="poster poster--offer offer-1">
  <svg class="poster__shapes" viewBox="0 0 344 468" preserveAspectRatio="none" aria-hidden="true">
    <path d="M0 150 C90 168 170 208 262 200 C200 232 90 236 0 222 Z" fill="var(--ink)"/>
    <path d="M344 172 C300 228 220 250 150 246 C232 232 300 206 344 160 Z" fill="var(--red)"/>
    <path d="M0 345 C120 318 250 330 344 352 L344 394 C250 370 120 362 0 386 Z" fill="var(--red)"/>
    <path d="M0 392 C120 370 250 378 344 400 L344 468 L0 468 Z" fill="var(--ink)"/>
  </svg>
  <h2 class="brand-name">LINDWERK</h2>
  <p class="brand-tagline">HAUSHALTSHILFEN &amp; MEHR</p>
  <div class="emblem"></div>
  <p class="offer-text"><span class="accent">HAUSHALTSHILFEN &amp;</span><br>ALLTAGSBEGLEITER</p>
  <p class="cta-label">Buchen Sie gleich einen Termin:</p>
  <p class="cta-phone"><svg class="phone-icon" viewBox="0 0 24 24"><circle cx="12" cy="12" r="12" fill="var(--red)"/><path d="M8.2 6.5c.5-.4 1.2-.3 1.5.2l1.2 2c.3.5.1 1.1-.3 1.4l-.8.6c.6 1.4 1.7 2.6 3.1 3.3l.7-.8c.4-.4 1-.5 1.4-.2l2 1.3c.5.3.6 1 .2 1.5l-.9 1c-.6.6-1.5.8-2.3.5-3.2-1.2-5.6-3.7-6.7-6.9-.3-.8 0-1.7.6-2.2z" fill="#fff"/></svg>0711 20 30 40 50</p>
  <p class="cta-web">www.lindwerk-hilfe.de</p>
</section>

<section class="poster poster--offer offer-2">
  <svg class="poster__shapes" viewBox="0 0 344 468" preserveAspectRatio="none" aria-hidden="true">
    <path d="M0 150 C90 168 170 208 262 200 C200 232 90 236 0 222 Z" fill="var(--ink)"/>
    <path d="M344 172 C300 228 220 250 150 246 C232 232 300 206 344 160 Z" fill="var(--red)"/>
    <path d="M0 345 C120 318 250 330 344 352 L344 394 C250 370 120 362 0 386 Z" fill="var(--red)"/>
    <path d="M0 392 C120 370 250 378 344 400 L344 468 L0 468 Z" fill="var(--ink)"/>
  </svg>
  <h2 class="brand-name">LINDWERK</h2>
  <p class="brand-tagline">HAUSHALTSHILFEN &amp; MEHR</p>
  <div class="emblem"></div>
  <p class="offer-text"><span class="accent">HAUSHALTSHILFEN</span><br>UND ALTAGSBEGLEITER<br>AB PFLEGEGRAD 1</p>
  <p class="cta-label">Buchen Sie gleich einen Termin:</p>
  <p class="cta-phone"><svg class="phone-icon" viewBox="0 0 24 24"><circle cx="12" cy="12" r="12" fill="var(--red)"/><path d="M8.2 6.5c.5-.4 1.2-.3 1.5.2l1.2 2c.3.5.1 1.1-.3 1.4l-.8.6c.6 1.4 1.7 2.6 3.1 3.3l.7-.8c.4-.4 1-.5 1.4-.2l2 1.3c.5.3.6 1 .2 1.5l-.9 1c-.6.6-1.5.8-2.3.5-3.2-1.2-5.6-3.7-6.7-6.9-.3-.8 0-1.7.6-2.2z" fill="#fff"/></svg>0711 20 30 40 50</p>
  <p class="cta-web">www.lindwerk-hilfe.de</p>
</section>

<section class="poster poster--offer offer-3">
  <svg class="poster__shapes" viewBox="0 0 344 468" preserveAspectRatio="none" aria-hidden="true">
    <path d="M0 150 C90 168 170 208 262 200 C200 232 90 236 0 222 Z" fill="var(--ink)"/>
    <path d="M344 172 C300 228 220 250 150 246 C232 232 300 206 344 160 Z" fill="var(--red)"/>
    <path d="M0 345 C120 318 250 330 344 352 L344 394 C250 370 120 362 0 386 Z" fill="var(--red)"/>
    <path d="M0 392 C120 370 250 378 344 400 L344 468 L0 468 Z" fill="var(--ink)"/>
  </svg>
  <h2 class="brand-name">LINDWERK</h2>
  <p class="brand-tagline">HAUSHALTSHILFEN &amp; MEHR</p>
  <div class="emblem"></div>
  <p class="offer-text">ABRECHNUNG MIT<br><span class="accent">ALLEN PFLEGEKASSEN</span></p>
  <p class="cta-label">Buchen Sie gleich einen Termin:</p>
  <p class="cta-phone"><svg class="phone-icon" viewBox="0 0 24 24"><circle cx="12" cy="12" r="12" fill="var(--red)"/><path d="M8.2 6.5c.5-.4 1.2-.3 1.5.2l1.2 2c.3.5.1 1.1-.3 1.4l-.8.6c.6 1.4 1.7 2.6 3.1 3.3l.7-.8c.4-.4 1-.5 1.4-.2l2 1.3c.5.3.6 1 .2 1.5l-.9 1c-.6.6-1.5.8-2.3.5-3.2-1.2-5.6-3.7-6.7-6.9-.3-.8 0-1.7.6-2.2z" fill="#fff"/></svg>0711 20 30 40 50</p>
  <p class="cta-web">www.lindwerk-hilfe.de</p>
</section>

<!-- Row 2: info posters -->
<section class="poster poster--info info-1">
  <svg class="poster__shapes" viewBox="0 0 344 550" preserveAspectRatio="none" aria-hidden="true">
    <path d="M0 82 L344 82 L344 250 C344 420 260 515 172 515 C84 515 0 420 0 250 Z" fill="var(--red)"/>
    <path d="M0 82 L344 82 L344 262 C344 410 260 490 172 490 C84 490 0 410 0 262 Z" fill="var(--paper)"/>
  </svg>
  <div class="info-head"><span class="dot"></span><div class="lockup"><span class="brand-name">LINDWERK</span><span class="brand-tagline">HAUSHALTSHILFEN &amp; MEHR</span></div></div>
  <p class="info-text">NUTZEN SIE IHREN ENTLASTUNGSBETRAG AB PFLEGEGRAD 1 UND IHRE VERHINDERUNGSPFLEGE AB DEM PFLEGEGRAD 2, <span class="dark">BEVOR IHR ANSPRUCH VERFÄLLT</span></p>
  <div class="emblem"></div>
</section>

<section class="poster poster--door">
  <svg class="poster__shapes" viewBox="0 0 344 784" preserveAspectRatio="none" aria-hidden="true">
    <rect x="0" y="165" width="344" height="480" fill="var(--paper)"/>
    <path d="M0 510 C40 635 304 635 344 510 L344 540 C300 660 44 660 0 540 Z" fill="var(--red)"/>
    <path d="M0 540 C44 660 300 660 344 540 L344 560 C300 672 44 672 0 560 Z" fill="var(--ink)"/>
  </svg>
  <div class="emblem"></div>
  <h2 class="brand-name">LINDWERK</h2>
  <p class="brand-tagline">HAUSHALTSHILFEN &amp; MEHR</p>
  <p class="cta-label">Buchen Sie gleich einen Termin:</p>
  <p class="door-phone"><svg class="phone-icon" viewBox="0 0 24 24"><circle cx="12" cy="12" r="12" fill="var(--red)"/><path d="M8.2 6.5c.5-.4 1.2-.3 1.5.2l1.2 2c.3.5.1 1.1-.3 1.4l-.8.6c.6 1.4 1.7 2.6 3.1 3.3l.7-.8c.4-.4 1-.5 1.4-.2l2 1.3c.5.3.6 1 .2 1.5l-.9 1c-.6.6-1.5.8-2.3.5-3.2-1.2-5.6-3.7-6.7-6.9-.3-.8 0-1.7.6-2.2z" fill="#fff"/></svg>0711 20 30 40 50</p>
</section>

<section class="poster poster--info info-2">
  <svg class="poster__shapes" viewBox="0 0 344 550" preserveAspectRatio="none" aria-hidden="true">
    <path d="M0 82 L344 82 L344 250 C344 420 260 515 172 515 C84 515 0 420 0 250 Z" fill="var(--red)"/>
    <path d="M0 82 L344 82 L344 262 C344 410 260 490 172 490 C84 490 0 410 0 262 Z" fill="var(--paper)"/>
  </svg>
  <div class="info-head"><span class="dot"></span><div class="lockup"><span class="brand-name">LINDWERK</span><span class="brand-tagline">HAUSHALTSHILFEN &amp; MEHR</span></div></div>
  <p class="info-text">HAUSHALTSHILFEN UND ALTAGSBEGLEITER AB PFLEGEGRAD 1</p>
  <p class="info-sub">BUCHEN SIE GLEICH HIER EIN TERMIN.</p>
  <div class="emblem"></div>
</section>

</body>
</html>
```